Simple templates for management consulting firm

Vireo Advisors is a management consulting firm based in the DC area. We have all the basic templates but would like to tweak them so they look consistent.

Check us out at www.vireoadvisors-example.com

For this project we would like to get
a tweaked powerpoint template (header should be up)
a letter template for letters
a fax template

Current templates and our logo are attached.
Updates

We just increased the budget of this project.

We got questions about the project. Here are our thoughts on this one:

Please include the logo into the fax template. If you find improvements in the layout then feel free to make those. Let's not overthink this too much. Keep it simple :)

We like The powerpoint concept as is. The slide titles are for some reasons on the bottom. It seems to irritate some folks. If you can switch the slide titles to the top, keep the look and feel of the slides and work in the logo then that would be fantastic.

The letter head should include the following

Vireo Advisors, LLC Box 5817, Pine Hollow, VA 20499 Phone 555 814-2906, Fax 555 276 9143, www.vireoadvisors-example.com and the logo.

Again, let's keep it simple.

Thank you for considering this project.

We just realize that we are not necessarily inisting to use the red in the slides.
Any approach that would work with the logo will be considered.

Thanks for your creativity.

Target Market(s)

tech companies, Meridian 400, venture capitalists

Industry/Entity Type

Management Consulting

Requirements
Must have
• Keep it simple please

```html
<!DOCTYPE html>
<html lang="en">
<head>
<meta charset="utf-8">
<title>Getting Projects Done – Vireo Advisors</title>
<link rel="stylesheet" href="https://fonts.googleapis.com/css2?family=PT+Sans:wght@700&family=Roboto+Condensed:ital,wght@0,400;1,700&display=swap">
<style>
  :root {
    --bg-light: #f7f7f7;
    --bg-dark: #cfcfcf;
    --title-grey: #8a8a8a;
    --title-shadow: #4a4a4a;
    --gold: #e9b52f;
    --gold-light: #f6dc86;
    --gold-deep: #a88a2e;
    --hex-edge: #6e6e6e;
    --label-grey: #6b6b6b;
    --rule-grey: #9a9a9a;
    --footer-ink: #333333;
    --brand-grey: #8c8c8c;
  }
  * { margin: 0; padding: 0; box-sizing: border-box; }
  html, body { width: 1200px; height: 816px; overflow: hidden; }
  body {
    position: relative;
    background: radial-gradient(ellipse at 50% 35%, var(--bg-light) 0%, #e6e6e6 55%, var(--bg-dark) 100%);
    font-family: "Roboto Condensed", "Arial Narrow", sans-serif;
  }
  .slide-title {
    position: absolute;
    left: 92px; top: 14px;
    font-family: "PT Sans", Arial, sans-serif;
    font-weight: 700;
    font-size: 92px;
    letter-spacing: 1px;
    color: var(--title-grey);
    text-shadow: 2px 3px 3px var(--title-shadow), -1px -1px 0 #d9d9d9;
    white-space: nowrap;
  }
  .title-bar {
    position: absolute;
    left: 91px; top: 128px;
    width: 810px; height: 18px;
    background: linear-gradient(to bottom, var(--gold-light), var(--gold) 50%, var(--gold-deep));
    box-shadow: 3px 4px 3px rgba(0,0,0,0.55);
  }
  .brand {
    position: absolute;
    left: 922px; top: 106px;
    display: flex; align-items: center; gap: 12px;
  }
  .brand-mark {
    width: 52px; height: 52px; border-radius: 50%;
    background: var(--brand-grey);
  }
  .brand-name {
    font-family: "PT Sans", Arial, sans-serif;
    font-weight: 700;
    font-size: 30px;
    color: var(--brand-grey);
    white-space: nowrap;
  }
  .crisis-map { position: absolute; left: 0; top: 0; }
  .hex-label {
    font-family: "Roboto Condensed", "Arial Narrow", sans-serif;
    font-style: italic; font-weight: 700;
    font-size: 19px; fill: var(--label-grey);
    text-anchor: middle;
  }
  .crisis-label {
    font-family: "PT Sans", Arial, sans-serif;
    font-style: italic; font-weight: 700;
    font-size: 62px; fill: var(--gold);
    text-anchor: middle;
  }
  .footer-rule {
    position: absolute; left: 49px; top: 748px;
    width: 1068px; height: 1px; background: var(--rule-grey);
  }
  .copyright {
    position: absolute; left: 0; top: 754px; width: 1200px;
    text-align: center;
    font-size: 18px; line-height: 18px;
    color: var(--footer-ink);
  }
</style>
</head>
<body>
  <h1 class="slide-title">Getting Projects DONE</h1>
  <div class="title-bar"></div>
  <div class="brand">
    <span class="brand-mark"></span>
    <span class="brand-name">Vireo Advisors</span>
  </div>

  <svg class="crisis-map" width="1200" height="816" viewBox="0 0 1200 816" aria-label="Causes of crisis">
    <defs>
      <linearGradient id="hexGold" x1="0" y1="0" x2="0" y2="1">
        <stop offset="0" stop-color="#f8f0cf"/>
        <stop offset="0.45" stop-color="#d9c27a"/>
        <stop offset="1" stop-color="#8f7a3a"/>
      </linearGradient>
      <linearGradient id="hexDark" x1="0" y1="0" x2="0" y2="1">
        <stop offset="0" stop-color="#f0f0f0"/>
        <stop offset="0.45" stop-color="#8a8a8a"/>
        <stop offset="1" stop-color="#2e2e2e"/>
      </linearGradient>
    </defs>

    <g class="connector-lines" fill="none" stroke="#6e6e6e" stroke-width="2">
      <polyline points="470,245 496,205 610,222"/>
      <polyline points="520,345 470,345 430,300"/>
      <polyline points="618,332 655,272 760,272"/>
      <polyline points="300,375 340,415 410,415"/>
      <polyline points="450,635 370,620 335,560"/>
      <polyline points="617,510 650,455 730,448"/>
      <polyline points="765,435 730,500 730,560"/>
      <polyline points="450,520 470,545 560,545"/>
      <polyline points="610,640 640,585 590,560"/>
      <polyline points="465,470 500,485 520,470"/>
    </g>

    <g class="hex-ring" stroke="var(--hex-edge)" stroke-width="7" fill="url(#hexGold)">
      <polygon points="610,268 573,205 500,205 464,268 500,331 573,331"/>
      <polygon points="766,360 730,297 657,297 620,360 657,423 730,423"/>
      <polygon points="766,537 730,474 657,474 620,537 657,600 730,600"/>
      <polygon points="613,621 577,558 504,558 467,621 504,684 577,684"/>
      <polygon points="457,533 421,470 348,470 311,533 348,596 421,596"/>
      <polygon points="457,360 421,297 348,297 311,360 348,423 421,423"/>
    </g>

    <polygon points="640,446 590,361 492,361 442,446 492,531 590,531"
             fill="url(#hexDark)" stroke="var(--hex-edge)" stroke-width="7"/>

    <text class="hex-label" x="537" y="266">Weak Financial</text>
    <text class="hex-label" x="537" y="289">Controls</text>
    <text class="hex-label" x="693" y="357">Sluggish Sales</text>
    <text class="hex-label" x="693" y="380">Force</text>
    <text class="hex-label" x="693" y="533">Changing</text>
    <text class="hex-label" x="693" y="556">Markets</text>
    <text class="hex-label" x="540" y="617">High Cost</text>
    <text class="hex-label" x="540" y="640">Structure</text>
    <text class="hex-label" x="384" y="538">Competition</text>
    <text class="hex-label" x="384" y="354">Ineffective</text>
    <text class="hex-label" x="384" y="377">Management</text>

    <text class="crisis-label" x="538" y="465">Crisis</text>
  </svg>

  <div class="footer-rule"></div>
  <p class="copyright">Copyright © 2012 by Vireo Advisors, LLC. All rights reserved. This document contains confidential and proprietary information and may not be<br>reproduced, in whole or in part, without express written permission from Vireo Advisors, LLC.</p>
</body>
</html>
```